"Brightwall Sound Living Residences" need a busines Card Design got Builder

We need a business card design for a company based in Milford, Michigancalled Brightwall Sound Living Residences - has been recognized as a premier custom home builder. Distinguished by outstanding craftmanship and timeless beauty. Our custom home can be found in the most prestigious communities in Michigan. The homes are built with ICF (insulated concrete homes) which is green, allergy free, fire free, mold free and quitter. Our slogan "building one dream at a Time" and also we are ICF distributor for the state of Michigan

Target Market(s)

Anyone who is making over $100,000 a year and who wants to have totally custom built home. Ages from 29 up to 60 years old

Industry/Entity Type

Concrete

Contact Information for Business Card

we want to use - green, black, gray or blue colors - we want to look different with our business cards, because we built homes only with ICF, green, healthier and highly energy efficient homes.

Requirements
Must have
• I have logo that I attached and we have been using the logo (the only green home)
Nice to have
• should look quality business card,

Files

```html
<!DOCTYPE html>
<html lang="en">
<head>
<meta charset="utf-8">
<title>Brightwall Sound Living Residences – Business Card</title>
<link rel="stylesheet" href="https://fonts.googleapis.com/css2?family=Jura:wght@400;600;700&display=swap">
<style>
  :root {
    --page: #e9eaed;
    --card: #ffffff;
    --navy: #2c2f8a;
    --royal: #2a55a8;
    --sky: #4f8fd6;
    --ink: #1f2024;
    --grey: #8a8c90;
    --title: #3d7fd0;
    --white: #ffffff;
  }
  * { margin: 0; padding: 0; box-sizing: border-box; }
  html, body { width: 1200px; height: 901px; overflow: hidden; }
  body {
    background: var(--page);
    font-family: "Jura", sans-serif;
    position: relative;
  }
  .card {
    position: absolute;
    left: 100px; top: 160px;
    width: 1000px; height: 580px;
    background: var(--card);
    border-radius: 48px;
    overflow: hidden;
    box-shadow: 0 10px 30px rgba(0,0,0,0.12);
  }
  .card-waves { position: absolute; inset: 0; width: 1000px; height: 580px; }
  .brand {
    position: absolute;
    left: 150px; top: 46px;
    width: 300px;
    text-align: center;
  }
  .brand-dot {
    width: 92px; height: 92px;
    border-radius: 50%;
    background: var(--navy);
    margin: 0 auto 14px;
  }
  .brand-name {
    font-weight: 600;
    font-size: 26px;
    line-height: 1.05;
    color: var(--grey);
    text-transform: uppercase;
    letter-spacing: 0.5px;
  }
  .person {
    position: absolute;
    left: 120px; top: 246px;
  }
  .person-name {
    font-weight: 700;
    font-size: 34px;
    color: var(--ink);
    letter-spacing: 1px;
    text-transform: uppercase;
  }
  .person-role {
    font-weight: 600;
    font-size: 24px;
    color: var(--title);
    margin-top: 0;
    margin-left: 16px;
  }
  .contact {
    position: absolute;
    right: 60px; top: 352px;
    color: var(--white);
    text-align: right;
  }
  .contact-address {
    font-weight: 600;
    font-size: 20px;
    line-height: 1.3;
    margin-bottom: 16px;
  }
  .contact-line {
    display: flex;
    justify-content: flex-end;
    align-items: center;
    gap: 10px;
    font-weight: 600;
    font-size: 18px;
    height: 27px;
  }
  .contact-line.small { font-size: 16px; height: 25px; }
  .contact-icon { width: 17px; height: 17px; flex: none; }
</style>
</head>
<body>
  <main class="card">
    <svg class="card-waves" viewBox="0 0 1000 580" aria-hidden="true">
      <defs>
        <linearGradient id="bandGradient" x1="0" y1="0" x2="1" y2="0">
          <stop offset="0" stop-color="#2c3a96"/>
          <stop offset="0.5" stop-color="#2a58ad"/>
          <stop offset="1" stop-color="#2c2f8a"/>
        </linearGradient>
      </defs>
      <path class="wave-light" d="M0,275 C150,345 320,395 540,402 C320,410 150,390 0,335 Z" fill="#4f8fd6"/>
      <path class="wave-band" d="M0,360 C180,420 360,445 520,428 C700,410 820,252 1000,225 L1000,580 L0,580 Z" fill="url(#bandGradient)"/>
      <path class="wave-line" d="M560,408 C720,386 830,232 1000,204" fill="none" stroke="#2a55a8" stroke-width="5"/>
    </svg>

    <div class="brand">
      <div class="brand-dot"></div>
      <div class="brand-name">Brightwall Sound<br>Living Residences</div>
    </div>

    <div class="person">
      <div class="person-name">Daniel Mercer</div>
      <div class="person-role">Managing Director</div>
    </div>

    <div class="contact">
      <div class="contact-address">214, 3rd floor, Elm Park<br>Avenue MFD</div>
      <div class="contact-line">012 555 0147
        <svg class="contact-icon" viewBox="0 0 24 24"><path fill="#fff" d="M6.6 10.8a15 15 0 0 0 6.6 6.6l2.2-2.2c.3-.3.7-.4 1-.2 1.1.4 2.3.6 3.6.6.6 0 1 .4 1 1V20c0 .6-.4 1-1 1A17 17 0 0 1 3 4c0-.6.4-1 1-1h3.5c.6 0 1 .4 1 1 0 1.3.2 2.5.6 3.6.1.3 0 .7-.2 1z"/></svg>
      </div>
      <div class="contact-line">012 555 0148
        <svg class="contact-icon" viewBox="0 0 24 24"><rect x="6" y="2" width="12" height="20" rx="2" fill="none" stroke="#fff" stroke-width="2"/><circle cx="12" cy="18" r="1.2" fill="#fff"/></svg>
      </div>
      <div class="contact-line">012 555 0149
        <svg class="contact-icon" viewBox="0 0 24 24"><rect x="3" y="8" width="18" height="12" rx="1" fill="#fff"/><rect x="7" y="3" width="10" height="6" fill="none" stroke="#fff" stroke-width="2"/></svg>
      </div>
      <div class="contact-line small">hello@brightwallsound.com
        <svg class="contact-icon" viewBox="0 0 24 24"><rect x="2" y="5" width="20" height="14" rx="1" fill="#fff"/><path d="M2 6l10 7 10-7" fill="none" stroke="#2c2f8a" stroke-width="1.6"/></svg>
      </div>
      <div class="contact-line small">www.brightwallsound.com
        <svg class="contact-icon" viewBox="0 0 24 24"><circle cx="12" cy="12" r="9" fill="none" stroke="#fff" stroke-width="2"/><path d="M3 12h18M12 3c3 3 3 15 0 18M12 3c-3 3-3 15 0 18" fill="none" stroke="#fff" stroke-width="1.5"/></svg>
      </div>
    </div>
  </main>
</body>
</html>
```